Real Estate Sign Project

We need a Real Estate sign that promotes the property being listed and our company and agent listing the property. The images need to be able to be swapped out so we can use the template for each listing we have. I have a sample from another company that shows what were are trying to accomplish. Would want ours to be unique using our logo and the colors in our logo. We would like to not have to use a rider. Would want agents name and phone number to be part of the 36" x 24" sign.

Industry/Entity Type

Real Estate

Requirements
Must have
• Sign dimensions are 36 inches by 24 inches (36" across and 24" up down). Use example.of.sign.we.want.jpg as the direction we want to go but with a different layout and our logo and colors. This would be just a template that we can swap out new pictures, address, price, website, agents contact info for each home we are listing. Like the idea of the pictures bleeding off the sides. Please use free stock photos for the home images as we will be changing these out for each listing. Please incorporate all info including agents info into the one sign. File must be layered so we can change the pictures, price, website, agent, etc. We use GIMP (.xcf) file

```html
<!DOCTYPE html>
<html lang="en">
<head>
<meta charset="utf-8">
<title>Home For Sale – Yard Sign</title>
<link rel="stylesheet" href="https://fonts.googleapis.com/css2?family=Libre+Baskerville:wght@400;700&family=Roboto+Condensed:wght@400;700&family=Open+Sans:wght@700;800&display=swap">
<style>
  :root{
    --backdrop:#e6e6e6;
    --orange:#f5681f;
    --blue:#1566ad;
    --navy:#1a3f85;
    --white:#ffffff;
    --sky:#3f7fd0;
    --stucco:#d4bc95;
    --lawn:#4f6b34;
    --cream:#ece4d3;
    --wood:#a8602c;
    --wood-dark:#6a3f22;
    --tile:#a57650;
  }
  *{box-sizing:border-box;margin:0;padding:0}
  html,body{width:1200px;height:900px;overflow:hidden;background:var(--backdrop)}
  .sign{position:absolute;left:129px;top:136px;width:942px;height:628px;background:var(--white)}

  .photo{position:absolute}
  .photo--exterior{left:0;top:0;width:597px;height:280px;
    background:linear-gradient(180deg,var(--sky) 0%,var(--sky) 12%,var(--stucco) 30%,var(--stucco) 86%,var(--lawn) 100%)}
  .photo--living{left:0;top:346px;width:219px;height:128px;
    background:linear-gradient(180deg,var(--cream) 0%,var(--tile) 100%)}
  .photo--bath{left:0;top:483px;width:219px;height:145px;
    background:linear-gradient(180deg,var(--tile) 0%,var(--wood-dark) 100%)}
  .photo--kitchen{left:227px;top:346px;width:184px;height:282px;
    background:linear-gradient(180deg,var(--wood) 0%,var(--wood) 70%,var(--cream) 100%)}
  .photo--dining{left:419px;top:346px;width:178px;height:282px;
    background:linear-gradient(180deg,var(--cream) 0%,var(--cream) 45%,var(--wood) 100%)}

  .feature-band{position:absolute;left:0;top:286px;width:564px;height:54px}
  .feature-band svg{position:absolute;inset:0}
  .address{position:absolute;left:14px;top:14px;font:400 24px/1 "Roboto Condensed",Arial,sans-serif;color:var(--white)}
  .specs{position:absolute;left:217px;top:5px;font:400 16.5px/22px "Roboto Condensed",Arial,sans-serif;color:var(--white);letter-spacing:.2px}
  .specs .sep{margin:0 7px}

  .panel{position:absolute;background:var(--orange);color:var(--white);text-align:center}
  .panel--headline{left:605px;top:0;width:337px;height:211px}
  .headline-main{margin-top:28px;font:700 74px/1 "Libre Baskerville",Georgia,serif;letter-spacing:1px}
  .headline-sub{margin-top:10px;font:700 46px/1 "Libre Baskerville",Georgia,serif;letter-spacing:1px}

  .brand-box{position:absolute;left:567px;top:211px;width:375px;height:204px;background:var(--white);
    display:flex;flex-direction:column;align-items:center;padding-top:26px}
  .brand-dot{width:62px;height:62px;border-radius:50%;background:var(--orange)}
  .brand{margin-top:14px;font:800 40px/1 "Open Sans",Arial,sans-serif;color:var(--navy);letter-spacing:.3px}
  .website{margin-top:14px;font:700 21px/1 "Open Sans",Arial,sans-serif;color:var(--blue)}
  .notch{position:absolute;left:754px;width:46px;height:28px}
  .notch--top{top:184px}
  .notch--bottom{top:414px}

  .panel--contact{left:605px;top:415px;width:337px;height:213px}
  .price{margin-top:45px;font:700 34px/1 "Libre Baskerville",Georgia,serif}
  .agent{margin-top:20px;font:400 26px/1 "Roboto Condensed",Arial,sans-serif;display:flex;justify-content:center;align-items:center}
  .agent strong{font-weight:700}
  .agent .rule{display:inline-block;width:2px;height:28px;background:var(--white);margin:0 10px}
  .phone{margin-top:23px;font:700 26px/1 "Roboto Condensed",Arial,sans-serif;letter-spacing:.5px}
</style>
</head>
<body>
<main class="sign">
  <div class="photo photo--exterior" role="img" aria-label="Exterior photo of the listed two-storey house"></div>

  <div class="feature-band">
    <svg width="564" height="54" viewBox="0 0 564 54" aria-hidden="true"><polygon points="0,0 536,0 564,27 536,54 0,54" fill="var(--blue)"/></svg>
    <div class="address">1720 Willow Lane</div>
    <div class="specs">4 Bedrooms<span class="sep">|</span>3.5 Baths<span class="sep">|</span>3200 Finished SF<br>2-Car Garage</div>
  </div>

  <div class="photo photo--living" role="img" aria-label="Living room photo"></div>
  <div class="photo photo--bath" role="img" aria-label="Bathroom photo"></div>
  <div class="photo photo--kitchen" role="img" aria-label="Kitchen photo"></div>
  <div class="photo photo--dining" role="img" aria-label="Breakfast bar and dining area photo"></div>

  <section class="panel panel--headline">
    <div class="headline-main">HOME</div>
    <div class="headline-sub">FOR SALE</div>
  </section>

  <section class="brand-box">
    <span class="brand-dot"></span>
    <div class="brand">Kestrel Homes</div>
    <div class="website">www.kestrelhomes.com</div>
  </section>
  <svg class="notch notch--top" viewBox="0 0 46 28" aria-hidden="true"><polygon points="0,28 23,0 46,28" fill="var(--white)"/></svg>

  <section class="panel panel--contact">
    <div class="price">$ 250,000 Only</div>
    <div class="agent">Agent<span class="rule"></span><strong>Mark Ellison</strong></div>
    <div class="phone">555/318-2046</div>
  </section>
  <svg class="notch notch--bottom" viewBox="0 0 46 28" aria-hidden="true"><polygon points="0,0 46,0 23,28" fill="var(--white)"/></svg>
</main>
</body>
</html>
```